banners,restaurant takeaway menu,catering packages for function room and takeaway

We are running indian restaurant in sydney and want to put feather type flags around our boundary.

1. we want to design 5 feather type flag specs
450*1620 mm
shape and image of flag inserted with material
2. Takeaway Menu update
3. Improving layout and redesisgning function menu with packages
4. Improving layout and redsigning of takeaway catering packages

notes

you can use pictures from from restaurant menu or the building pics as available from our restaurant or any better ideas you have

```html
<!DOCTYPE html>
<html lang="en">
<head>
<meta charset="utf-8">
<title>Saffron Leaf – Feather Flag Set</title>
<link rel="stylesheet" href="https://fonts.googleapis.com/css2?family=Montserrat:wght@700;800&family=Oswald:wght@300;400;500;600&family=Playfair+Display:wght@700&display=swap">
<style>
  :root {
    --saffron: #f0a035;
    --leaf: #1c8a43;
    --royal: #1565c0;
    --ink: #1a1a1a;
    --gold: #b8892e;
    --paper: #ffffff;
    --canvas: #ffffff;
  }
  * { margin: 0; padding: 0; box-sizing: border-box; }
  html, body {
    width: 729px; height: 1200px; overflow: hidden;
    background: var(--canvas);
  }
  .flag-set {
    width: 729px; height: 1200px;
    display: flex; align-items: center; justify-content: center;
    gap: 21px;
  }
  .flag {
    width: 160px; height: 576px;
    background: var(--paper);
    box-shadow: 0 2px 10px rgba(0,0,0,0.12);
    overflow: hidden;
  }
  .flag svg { display: block; width: 160px; height: 576px; overflow: hidden; }
  .t-display { font-family: "Montserrat", sans-serif; font-weight: 800; }
  .t-condensed { font-family: "Oswald", sans-serif; font-weight: 500; }
  .t-condensed-light { font-family: "Oswald", sans-serif; font-weight: 300; }
  .t-brand { font-family: "Oswald", sans-serif; font-weight: 400; fill: var(--ink); }
  .t-script { font-family: "Playfair Display", serif; font-weight: 700; fill: var(--gold); }
  .fill-saffron { fill: var(--saffron); }
  .fill-leaf { fill: var(--leaf); }
  .fill-royal { fill: var(--royal); }
  .fill-white { fill: #ffffff; }
  .fill-ink { fill: var(--ink); }
</style>
</head>
<body>
<main class="flag-set">

  <!-- Flag: opening hours -->
  <section class="flag flag--hours">
    <svg viewBox="0 0 160 576">
      <defs>
        <linearGradient id="dishes-hours" x1="0" y1="0" x2="1" y2="1">
          <stop offset="0" stop-color="#e7c79a"/>
          <stop offset="0.5" stop-color="#d9a05a"/>
          <stop offset="1" stop-color="#c9c9c4"/>
        </linearGradient>
      </defs>
      <path class="fill-saffron" d="M0 372 V95 Q4 48 50 30 V372 Z"/>
      <rect class="fill-leaf" x="108" y="0" width="52" height="372"/>
      <text class="t-display fill-white" font-size="33" transform="translate(40 350) rotate(-90)" textLength="235" lengthAdjust="spacingAndGlyphs">BREAKFAST</text>
      <text class="t-display fill-royal" font-size="33" transform="translate(92 350) rotate(-90)" textLength="150" lengthAdjust="spacingAndGlyphs">LUNCH</text>
      <text class="t-display fill-white" font-size="33" transform="translate(147 350) rotate(-90)" textLength="175" lengthAdjust="spacingAndGlyphs">DINNER</text>
      <g role="img" aria-label="Photo of South Indian breakfast plates: idli, vada, sambar and biryani">
        <rect x="0" y="362" width="160" height="104" fill="url(#dishes-hours)"/>
      </g>
      <text class="t-condensed fill-saffron" font-size="30" x="80" y="505" text-anchor="middle" textLength="112" lengthAdjust="spacingAndGlyphs">OPEN FOR</text>
      <text class="t-brand" font-size="15" x="80" y="555" text-anchor="middle">Saffron Leaf</text>
    </svg>
  </section>

  <!-- Flag: happy hours -->
  <section class="flag flag--happy-hours">
    <svg viewBox="0 0 160 576">
      <defs>
        <linearGradient id="drinks" x1="0" y1="0" x2="1" y2="0">
          <stop offset="0" stop-color="#d64a6a"/>
          <stop offset="0.35" stop-color="#d8c43a"/>
          <stop offset="0.65" stop-color="#9ccf7a"/>
          <stop offset="1" stop-color="#c0202e"/>
        </linearGradient>
      </defs>
      <text class="t-brand" font-size="16" x="80" y="65" text-anchor="middle">Saffron Leaf</text>
      <g class="promo-diagonal" transform="rotate(-34 80 230)">
        <text class="t-condensed fill-saffron" font-size="13" x="95" y="150" text-anchor="middle" textLength="88" lengthAdjust="spacingAndGlyphs">MONDAY - FRIDAY</text>
        <text class="t-condensed fill-leaf" font-size="13" x="100" y="166" text-anchor="middle">(5PM - 7PM)</text>
        <rect class="fill-saffron" x="-200" y="174" width="560" height="32"/>
        <text class="t-condensed fill-white" font-size="26" x="80" y="200" text-anchor="middle" textLength="138" lengthAdjust="spacingAndGlyphs">HAPPY HOURS</text>
        <rect class="fill-leaf" x="-200" y="212" width="560" height="26"/>
        <text class="t-condensed fill-saffron" font-size="25" x="80" y="266" text-anchor="middle" textLength="108" lengthAdjust="spacingAndGlyphs">ALL DRINKS</text>
        <text class="t-condensed fill-leaf" font-size="24" x="90" y="294" text-anchor="middle">$5.00</text>
      </g>
      <g role="img" aria-label="Photo of colourful mocktails in tall glasses with fruit">
        <rect x="0" y="386" width="160" height="96" fill="url(#drinks)"/>
      </g>
      <text class="t-condensed fill-saffron" font-size="25" x="80" y="512" text-anchor="middle" textLength="130" lengthAdjust="spacingAndGlyphs">ADD A CANAPE</text>
      <text class="t-condensed fill-ink" font-size="11" x="48" y="532">FOR</text>
      <text class="t-condensed fill-ink" font-size="11" x="46" y="545">JUST</text>
      <text class="t-condensed fill-leaf" font-size="33" x="70" y="548" textLength="56" lengthAdjust="spacingAndGlyphs">$6.50</text>
    </svg>
  </section>

  <!-- Flag: special lunch -->
  <section class="flag flag--special-lunch">
    <svg viewBox="0 0 160 576">
      <defs>
        <linearGradient id="curry-bowl" x1="0" y1="0" x2="0" y2="1">
          <stop offset="0" stop-color="#d8742c"/>
          <stop offset="1" stop-color="#b9b9b6"/>
        </linearGradient>
        <linearGradient id="thali" x1="0" y1="0" x2="1" y2="1">
          <stop offset="0" stop-color="#e0a850"/>
          <stop offset="1" stop-color="#d8d2c4"/>
        </linearGradient>
      </defs>
      <text class="t-brand" font-size="16" x="80" y="65" text-anchor="middle">Saffron Leaf</text>
      <polygon class="fill-saffron" points="0,228 150,100 150,145 0,280"/>
      <polygon class="fill-leaf" points="0,350 160,194 160,240 0,402"/>
      <g role="img" aria-label="Photo of paneer curry in a steel bowl">
        <ellipse cx="78" cy="150" rx="72" ry="55" fill="url(#curry-bowl)"/>
      </g>
      <g role="img" aria-label="Photo of a thali plate with curries, rice and roti">
        <ellipse cx="82" cy="280" rx="80" ry="62" fill="url(#thali)"/>
      </g>
      <text class="t-display fill-saffron" font-size="22" x="80" y="395" text-anchor="middle" textLength="124" lengthAdjust="spacingAndGlyphs">SPECIAL</text>
      <text class="t-display fill-leaf" font-size="29" x="80" y="425" text-anchor="middle" textLength="124" lengthAdjust="spacingAndGlyphs">LUNCH</text>
      <rect class="fill-saffron" x="30" y="436" width="100" height="40" rx="4"/>
      <text class="t-display fill-white" font-size="24" x="80" y="465" text-anchor="middle">$14.90</text>
      <text class="t-condensed-light fill-ink" font-size="15" x="80" y="499" text-anchor="middle">(VEG &amp; NON VEG)</text>
      <rect class="fill-leaf" x="30" y="510" width="100" height="22" rx="7"/>
      <text class="t-display fill-white" font-size="11" x="80" y="525" text-anchor="middle">AVAILABLE</text>
      <text class="t-display fill-leaf" font-size="11" x="80" y="550" text-anchor="middle">CURRY AND RICE</text>
    </svg>
  </section>

  <!-- Flag: seasonal greetings -->
  <section class="flag flag--season">
    <svg viewBox="0 0 160 576">
      <defs>
        <linearGradient id="festive-plate" x1="0" y1="0" x2="1" y2="1">
          <stop offset="0" stop-color="#d79a4c"/>
          <stop offset="0.5" stop-color="#efe6d8"/>
          <stop offset="1" stop-color="#c8a45a"/>
        </linearGradient>
        <linearGradient id="pine" x1="0" y1="0" x2="0" y2="1">
          <stop offset="0" stop-color="#ffffff"/>
          <stop offset="1" stop-color="#3f6b2a"/>
        </linearGradient>
      </defs>
      <polygon class="fill-saffron" points="67,92 160,24 160,56 67,124"/>
      <polygon class="fill-leaf" points="86,176 160,100 160,132 86,208"/>
      <g role="img" aria-label="Illustration of a hanging Christmas bauble">
        <circle cx="30" cy="130" r="16" fill="#b4472a"/>
      </g>
      <g role="img" aria-label="Photo of biryani, idli, vada and a thali plate">
        <rect x="0" y="212" width="160" height="176" fill="url(#festive-plate)"/>
      </g>
      <text class="t-brand" font-size="19" x="80" y="440" text-anchor="middle">Saffron Leaf</text>
      <text class="t-script" font-size="17" x="80" y="470" text-anchor="middle">Merry</text>
      <text class="t-script" font-size="19" x="80" y="489" text-anchor="middle">Christmas</text>
      <text class="t-script" font-size="5" x="80" y="498" text-anchor="middle" letter-spacing="1.2">&amp; HAPPY NEW YEAR</text>
      <g role="img" aria-label="Illustration of pine branches with golden baubles">
        <rect x="0" y="530" width="160" height="46" fill="url(#pine)"/>
      </g>
    </svg>
  </section>

</main>
</body>
</html>
```